Funeral Home Brochures, to attract and wow people to read the brochure.

We have a logo HBR (Harlow-Brent Mortuary, LLC)
A Trifold;
Need catch phases, pictures, services, Traditional Funerals, Graveside Services, Direct Cremation, Cremation with a Memorial Service.
Serving families of all nationalities.
Live Well Plan Ahead with Prearrangement of your service, relieving your family of the financial responsibilities. Prearrangement helps protect your family by freezing most of the costs for select products and services at today's prices.
Serving families with the Highest Quality at AFFORABLE PRICE.
Whatever ideas you have for the brochure that would catch my attention to pick up and read, call more information, etc.
You can also check see our website for more information.

```html
<!DOCTYPE html>
<html lang="en">
<head>
<meta charset="utf-8">
<title>Harlow-Brent Mortuary – Trifold Brochure</title>
<link href="https://fonts.googleapis.com/css2?family=Libre+Baskerville:wght@400;700&family=Lato:wght@300;400&display=swap" rel="stylesheet">
<style>
:root{
  --page:#b4c8dc;
  --page-deep:#a3bad2;
  --ink-dark:#2a2a2c;
  --paper:#ffffff;
  --navy:#2f4b64;
  --band:#3e5b74;
  --text-dark:#2b2b2b;
  --text-light:#ececec;
  --muted:#4a4a4a;
}
*{margin:0;padding:0;box-sizing:border-box}
html,body{width:858px;height:1200px;overflow:hidden}
body{background:linear-gradient(180deg,var(--page) 0%,var(--page-deep) 100%);font-family:'Lato',sans-serif;font-weight:300;color:var(--text-dark);position:relative}
.sheet{position:absolute;left:48px;width:762px;height:540px;box-shadow:0 4px 14px rgba(30,50,80,.25);overflow:hidden}
.sheet--outside{top:45px}
.sheet--inside{top:615px}
.panel{position:absolute;top:0;width:254px;height:540px;overflow:hidden}
.panel--1{left:0}.panel--2{left:254px}.panel--3{left:508px}
.dark{background:var(--ink-dark);color:var(--text-light)}
.light{background:var(--paper);color:var(--muted)}
.pad{padding:16px 13px 0 13px}
h2{font-family:'Libre Baskerville',serif;font-weight:700;font-size:12.6px;line-height:1.15;letter-spacing:-.2px}
.dark h2{color:#fff}
.light h2{color:var(--navy)}
.lead{font-weight:400;font-size:8.2px;line-height:11px;margin:6px 0 8px}
ul{list-style:none}
li{position:relative;padding-left:13px;font-size:8.1px;line-height:12.7px;margin-bottom:7px}
li::before{content:"";position:absolute;left:0;top:3px;width:5px;height:5px;border:1.3px solid #6f8ca6;border-radius:50%}
.dark li::before{border-color:#9bb3c9}
li.tight{margin-bottom:1px}
b{font-weight:400;color:inherit}
.light b{color:var(--text-dark)}
p.body{font-size:8.1px;line-height:11.8px}
/* outside */
.panel--2 .upper{background:var(--paper);height:354px;padding:16px 12px 0 12px;color:var(--muted)}
.panel--2 .upper h2{color:var(--navy);margin:14px 0 6px}
.panel--2 .lower{position:absolute;top:354px;left:0;right:0;bottom:0;padding:30px 12px 0}
.reach{font-family:'Libre Baskerville',serif;font-weight:700;font-size:18px;color:#fff;margin-bottom:12px}
.contact{display:flex;align-items:flex-start;gap:9px;font-size:10.6px;font-weight:400;line-height:13px;margin-bottom:8px;color:#f2f2f2}
.contact svg{flex:none;width:11px;height:11px;margin-top:1px}
.cover-photo{position:absolute;left:0;top:0;width:254px;height:270px;background:radial-gradient(ellipse at 35% 30%,#8a8580 0%,#4f4b48 45%,#2c2a29 100%)}
.brand{position:absolute;left:0;right:0;top:212px;text-align:center;color:#fff;font-family:'Lato',sans-serif;font-weight:400;font-size:15.5px;letter-spacing:1.5px;line-height:19px}
.band{position:absolute;left:0;top:270px;width:254px;height:60px;background:var(--band);color:#fff;text-align:center;font-family:'Libre Baskerville',serif;font-weight:700;font-size:15px;line-height:18px;padding-top:11px}
.cover-lower{position:absolute;left:0;top:330px;width:254px;height:210px;background:radial-gradient(ellipse at 40% 20%,#6d6f70 0%,#35363a 55%,#222 100%)}
.snap{position:absolute;background:#fff;padding:3px;box-shadow:0 2px 6px rgba(0,0,0,.5)}
.snap div{width:100%;height:100%}
/* inside */
.flag-photo{position:absolute;left:13px;top:17px;width:227px;height:143px;border-radius:3px;background:linear-gradient(160deg,#3d4f78 0%,#8f8a8f 50%,#b49a8a 75%,#7c6f62 100%)}
.soldier-photo{position:absolute;left:138px;top:71px;width:102px;height:118px;background:#fff;padding:3px;box-shadow:0 2px 6px rgba(0,0,0,.3)}
.soldier-photo div{width:100%;height:100%;background:linear-gradient(160deg,#d8d8d8,#6a6a6a 60%,#3a3a3a)}
.military{position:absolute;left:13px;right:13px;top:204px}
.military h2{margin-bottom:6px}
.military .lead{margin:0 0 4px}
.mid-top{padding:18px 12px 0}
.mid-top li{margin-bottom:9px;line-height:11.8px}
.collage{position:absolute;left:25px;top:219px;width:210px;height:142px}
.tile{position:absolute;background:#fff;padding:2px}
.tile div{width:100%;height:100%}
.odv-title{position:absolute;left:13px;top:376px;font-size:13px}
.odv-devices{position:absolute;left:28px;top:398px;width:200px;height:120px;background:linear-gradient(135deg,#bdb2a8 0%,#9e9189 60%,#4a4a4e 100%);border-radius:4px}
.right h2{font-size:13.6px;margin-bottom:10px}
.right .lead{margin:0 0 10px}
.right h3{font-family:'Libre Baskerville',serif;font-weight:700;font-size:8px;color:var(--text-dark);margin-bottom:8px}
.right p.body{margin-bottom:12px;line-height:12.7px}
</style>
</head>
<body>

<!-- Outside sheet -->
<section class="sheet sheet--outside">
  <div class="panel panel--1 dark pad">
    <h2>Burial Services</h2>
    <p class="lead">There are different elements you can choose from when arranging a burial, depending upon your individual needs and preferences:</p>
    <ul>
      <li>Immediate burial means that your loved one's physical remains will be buried or entombed without a public service or gathering.<br>A visitation, also called a viewing, wake or calling hours, allows family and friends to gather in a room with the departed loved one in an open or closed casket to say goodbye and offer their support and sympathy. We offer all night visitation for the traditional spanish service.</li>
      <li>Funeral or memorial services can take place at a funeral home, church, or even at your home. Whether traditional or unique, both the visitation and the service can be personalized to reflect your loved one. For more information on personalization, visit our page on celebrating life.</li>
      <li>Graveside, chapel, or committal services are held at the cemetery, and allow family and friends to be present for the burial if they wish.</li>
    </ul>
    <h2 style="margin-top:20px">Cremation Services</h2>
    <p class="lead">After the cremation, there are a variety of choices for your loved one's final disposition. Your decision will depend on your religious beliefs and personal preferences, but here are some options to consider:</p>
    <ul>
      <li>Interment means that you'll bury or entomb your loved one's cremated remains. This can be in a family plot, a memorial site, a cremation niche or urn garden, or in a variety of other indoor and outdoor locations. Ask our staff for a detailed list of local interment possibilities.</li>
      <li>Graveside services are similar to those celebrated alongside a traditional ground burial, in which loved ones are present at the burial of the cremated remains and honor the deceased through memorial prayers or other meaningful tributes.</li>
    </ul>
  </div>

  <div class="panel panel--2 dark">
    <div class="upper">
      <ul>
        <li>Scattering allows you to spread your loved one's cremated remains in a memorial garden, a cemetery, over water, or across any other meaningful site. You also can choose to scatter some of the cremated remains and retain the rest in an urn for internment or another form of disposition.</li>
        <li>Placing cremated remains in multiple urns allows family members who are separated by distance to each feel the comfort of having their loved one's final resting place in a nearby location.</li>
      </ul>
      <h2>Live Funeral Webcasting</h2>
      <p class="body">Webcasting your loved one's service gives those who are unable to travel the ability to see the service live or watch it later at their convenience.</p>
      <h2>The Healing Power<br>of a Memorial Service</h2>
      <p class="body">A funeral service provides those who are grieving with a supportive environment to celebrate their loved one's life and start the journey toward healing and peace. No matter what direction you choose, our staff is honored to assist you in creating a service that reflects your loved one's unique life journey.</p>
    </div>
    <div class="lower">
      <div class="reach">Reach Us!</div>
      <div class="contact"><svg viewBox="0 0 24 24" fill="none" stroke="#fff" stroke-width="2"><path d="M5 3h4l2 5-3 2a12 12 0 0 0 6 6l2-3 5 2v4a2 2 0 0 1-2 2A18 18 0 0 1 3 5a2 2 0 0 1 2-2z"/></svg><span>Phone: (555) 214-0808</span></div>
      <div class="contact"><svg viewBox="0 0 24 24" fill="none" stroke="#fff" stroke-width="2"><rect x="3" y="9" width="18" height="12" rx="1"/><path d="M7 9V3h10v6M7 13h2M11 13h2M15 13h2M7 17h2M11 17h2M15 17h2"/></svg><span>Fax (555) 214-0810</span></div>
      <div class="contact"><svg viewBox="0 0 24 24" fill="none" stroke="#fff" stroke-width="2"><path d="M12 22s7-7 7-12a7 7 0 0 0-14 0c0 5 7 12 7 12z"/><circle cx="12" cy="10" r="2.5"/></svg><span>612 North Alder<br>Westbrook, TX 77000</span></div>
      <div class="contact"><svg viewBox="0 0 24 24" fill="none" stroke="#fff" stroke-width="2"><rect x="3" y="4" width="18" height="16" rx="1"/><path d="M3 8h18"/></svg><span>harlowbrent.com</span></div>
    </div>
  </div>

  <div class="panel panel--3 dark">
    <div class="cover-photo" role="img" aria-label="Photo of a grieving older man in a dark suit at a funeral"></div>
    <div class="brand">HARLOW-BRENT<br>MORTUARY</div>
    <div class="band">Serving Families<br>With Grace &amp; Dignity</div>
    <div class="cover-lower" role="img" aria-label="Photo of white funeral flowers beside a casket"></div>
    <div class="snap" style="left:100px;top:420px;width:74px;height:96px;transform:rotate(-4deg)"><div role="img" aria-label="Family photo of a father hugging his child" style="background:linear-gradient(150deg,#c7b8a8,#7d6a5a)"></div></div>
    <div class="snap" style="left:171px;top:405px;width:66px;height:98px;transform:rotate(3deg)"><div role="img" aria-label="Family photo of a mother and daughter with their dog" style="background:linear-gradient(150deg,#d9cfc3,#8f7a65)"></div></div>
  </div>
</section>

<!-- Inside sheet -->
<section class="sheet sheet--inside">
  <div class="panel panel--1 light">
    <div class="flag-photo" role="img" aria-label="Photo of a hand resting on a folded American flag"></div>
    <div class="soldier-photo"><div role="img" aria-label="Black and white photo of a soldier holding a flag"></div></div>
    <div class="military">
      <h2>Standard Honor<br>Military Funerals</h2>
      <p class="lead">Traditional elements and honors can include the following:</p>
      <ul>
        <li class="tight">A <b>Military Chaplain</b> for family members.</li>
        <li class="tight">A <b>Flag Presentation Service</b> by the chaplain of the Veterans Honor Guild.</li>
        <li class="tight">A <b>Final Salute</b> at the gravesite.</li>
      </ul>
      <h2 style="margin-top:12px">Full Honor Military Funerals</h2>
      <p class="lead">Full elements and honors includes standard honors<br>&amp; the following:</p>
      <ul>
        <li class="tight">Depending on their rank, <b>A Three-Volley Salute.</b></li>
        <li class="tight"><b>The U.S. Flag Draped</b> over the casket and given to the next of kin following the service.</li>
        <li class="tight"><b>The Playing of Taps.</b></li>
      </ul>
      <h2 style="margin-top:14px">Grief Resources</h2>
      <p class="lead">The following are some tools available to assist you in your healing journey.</p>
      <ul>
        <li class="tight"><b>GriefCircle</b><br>GriefCircle is a friendly, caring group of people who will walk alongside you through one of life's most difficult experiences.</li>
      </ul>
    </div>
  </div>

  <div class="panel panel--2 dark">
    <div class="mid-top">
      <ul>
        <li><b>Online Healing</b><br>Online Healing offers grief discussion boards where men and women can discuss issues related to grief and healing or browse recommended grief books.</li>
        <li><b>The Kindred Parents Network</b><br>Whether your family has had a child die (at any age, from any cause), or you are helping those who have gone through this life-altering experience, The Kindred Parents Network exists to provide friendship, understanding, and hope to those going through the natural grieving process.</li>
        <li><b>Elder Care Alliance</b><br>With Elder Care Alliance, you'll find articles, discussions, and helpful information on dealing with end of life care, the challenges faced by caregivers, and how to deal with grief after a loss.</li>
      </ul>
    </div>
    <div class="collage">
      <div class="tile" style="left:0;top:0;width:89px;height:102px"><div role="img" aria-label="Photo of a hand holding a glowing digital icon" style="background:linear-gradient(150deg,#dfe4ea,#7f95ab)"></div></div>
      <div class="tile" style="left:122px;top:0;width:88px;height:102px"><div role="img" aria-label="Photo of a woman in white making a heart with her hands" style="background:linear-gradient(150deg,#f3f1ee,#bcb6ae)"></div></div>
      <div class="tile" style="left:61px;top:40px;width:88px;height:102px"><div role="img" aria-label="Photo of a video call with a man waving on a laptop" style="background:linear-gradient(150deg,#6e6a7a,#2e2a28 70%,#c08a55)"></div></div>
    </div>
    <h2 class="odv-title">The "Online Digital Version" (ODV)</h2>
    <div class="odv-devices" role="img" aria-label="Mockup of a digital memorial program shown on laptop, tablet and phone"></div>
  </div>

  <div class="panel panel--3 light pad right">
    <h2>Multicultural Options</h2>
    <p class="lead">We are dedicated to helping families of all faiths plan the most appropriate service, and assuring that the smallest detail is never overlooked in their time of need.</p>
    <h3>Respecting the Diversity of Your Family</h3>
    <p class="body">Harlow-Brent Mortuary celebrates the ethnic diversity of our community by offering a wide variety of options to meet the special religious and cultural traditions of families. Our professional staff has worked with leaders in the African American, Buddhist, Catholic, Hindu, Hispanic, Jewish and Protestant communities to make sure that religious guidelines are followed according to a family's wishes.</p>
    <p class="body">Some religious guidelines dictate that services take place as soon as possible after a death starting with a purification ceremony or by praying and watching over the deceased. For other cultures, it is customary to wait a week or more. Ritual chanting, singing, praying, music, readings, flowers, incense or candles are important to many. There are also those who give guests special mementos like an envelope with coins for good luck or candy to help take away the bitter taste of death. Many families mourn wearing black while in others the immediate family wears white.</p>
    <p class="body">There are funeral traditions that end with the family watching the casket lowered into the ground and others that specifically ask that family members not see the casket being lowered. Some choose to create their own contemporary rituals. Whether your family wishes to observe longstanding traditions, create new rituals or blend both together, our staff can help.</p>
    <p class="body">We've arranged services in our funeral homes, private homes, chapels, churches, temples, cemeteries, crematory chapels and other places meaningful to the person being honored. A funeral is more than a way to mourn a loss--it is also a collective celebration of a life well-lived.</p>
  </div>
</section>

</body>
</html>
```